Talvex Engineering Business card Design

We need to make business cards for our NDT and inspection company. The company is called Talvex Engineering. We want a professional modern feel business card. We have just completed the remaking of our website and would like to have business cards with the same feel and colours. The final design should communicate professionalism and cutting edge tech.

Target Market(s)

We sell to B2B Business clients. Our customer is an engineer or decision maker in the mechanical engineering / Oil and gas field.

Contact Information for Business Card

Please see the current business cards that we have uploaded to get the details. You can also look at our Website www.talvex-eng.example for more.

Requirements
Must have
• Less is more
Nice to have
• Less is more

```html
<!DOCTYPE html>
<html lang="en">
<head>
<meta charset="utf-8">
<title>Talvex Engineering Business Card</title>
<link href="https://fonts.googleapis.com/css2?family=Rajdhani:wght@700&family=Roboto:wght@400&display=swap" rel="stylesheet">
<style>
  :root {
    --page-bg: #e9e6e2;
    --card-bg: #f7f6f4;
    --brand-red: #b3171f;
    --brand-navy: #1f2f6b;
    --text-navy: #1e2a5a;
    --contact-text: #e3d9c8;
  }
  html, body {
    margin: 0;
    width: 1200px;
    height: 1054px;
    overflow: hidden;
    background: var(--page-bg);
  }
  .card {
    position: absolute;
    left: 100px;
    top: 225px;
    width: 1000px;
    height: 603px;
    background: var(--card-bg);
    box-shadow: 0 10px 30px rgba(0,0,0,0.15);
    overflow: hidden;
    font-family: "Roboto", sans-serif;
  }
  .card-band {
    position: absolute;
    inset: 0;
  }
  .brand {
    position: absolute;
    left: 80px;
    top: 222px;
    display: flex;
    align-items: center;
    gap: 16px;
  }
  .brand-dot {
    width: 34px;
    height: 34px;
    border-radius: 50%;
    background: var(--brand-red);
  }
  .brand-name {
    font-family: "Rajdhani", sans-serif;
    font-weight: 700;
    font-size: 44px;
    color: var(--brand-navy);
    line-height: 1;
  }
  .identity {
    position: absolute;
    right: 58px;
    top: 78px;
    text-align: right;
    color: var(--text-navy);
  }
  .person-name {
    font-family: "Rajdhani", sans-serif;
    font-weight: 700;
    font-size: 38px;
    color: var(--brand-red);
    line-height: 1.1;
  }
  .person-title {
    font-size: 24px;
    margin-top: 6px;
  }
  .address {
    font-size: 24px;
    line-height: 38px;
    margin-top: 38px;
  }
  .contacts {
    position: absolute;
    right: 58px;
    top: 440px;
    list-style: none;
    margin: 0;
    padding: 0;
    color: var(--contact-text);
    font-size: 24px;
    text-align: right;
  }
  .contacts li {
    display: flex;
    justify-content: flex-end;
    align-items: center;
    gap: 14px;
    height: 38px;
  }
  .contact-icon {
    width: 20px;
    height: 20px;
    fill: var(--contact-text);
  }
</style>
</head>
<body>
  <div class="card">
    <svg class="card-band" viewBox="0 0 1000 603" preserveAspectRatio="none">
      <polygon points="0,526 1000,341 1000,353 0,538" fill="var(--brand-red)"/>
      <polygon points="0,545 1000,360 1000,603 0,603" fill="var(--brand-navy)"/>
    </svg>

    <div class="brand">
      <span class="brand-dot"></span>
      <span class="brand-name">Talvex Engineering</span>
    </div>

    <div class="identity">
      <div class="person-name">Jonah Wekesa</div>
      <div class="person-title">Environmental Manager</div>
      <div class="address">P.O. BOX 40127-80100<br>Mombasa Kenya</div>
    </div>

    <ul class="contacts">
      <li>+ 254 20 555 0142/3
        <svg class="contact-icon" viewBox="0 0 24 24"><path d="M3 8c0-3 4-4 9-4s9 1 9 4v2h-5V8H8v2H3z"/><path d="M6 12h12l2 8H4z"/></svg>
      </li>
      <li>info@talvex-eng.example
        <svg class="contact-icon" viewBox="0 0 24 24"><path d="M2 5h20v14H2z M4 7v.5l8 6 8-6V7z" fill-rule="evenodd"/></svg>
      </li>
      <li>www.talvex-eng.example
        <svg class="contact-icon" viewBox="0 0 24 24"><circle cx="12" cy="12" r="9" fill="none" stroke="var(--contact-text)" stroke-width="2"/><path d="M3 12h18M12 3c-4 5-4 13 0 18M12 3c4 5 4 13 0 18" fill="none" stroke="var(--contact-text)" stroke-width="1.6"/></svg>
      </li>
    </ul>
  </div>
</body>
</html>
```